Silverleaf upkeep services strata flyer

Looking for a flyer that will grab peoples attention also need to include some kind off promotional offer on there so they will hold onto the flyer . Would like approximateley 4 pictures of appartment blocks. Would like to include the following services. Building management Common area cleaning ,window cleaning, lawn mowing, gardening , pressure cleaning, carpet cleaning, bin cleaning. Handy man services.

Target Market(s)

appartment blocks/strata managers

Industry/Entity Type

Pressure Cleaning

Font styles to use
Serif

Colors
0355a3
ceddec
ec2027

Requirements
Must have
• company logo & colors contact details email: Info@silverleafupkeepservices.com.au
• Phone: 0438507721 website silverleafupkeepservices.com.au

```html
<!DOCTYPE html>
<html lang="en">
<head>
<meta charset="utf-8">
<title>Silverleaf upkeep services – Strata Flyer</title>
<link href="https://fonts.googleapis.com/css2?family=Great+Vibes&family=Lora:ital,wght@0,700;1,700&family=Oswald:wght@600&family=Open+Sans:wght@400&display=swap" rel="stylesheet">
<style>
  :root {
    --brand-blue: #0355a3;
    --brand-blue-dark: #02386f;
    --brand-mist: #ceddec;
    --brand-red: #ec2027;
    --ink: #1c1c1c;
    --white: #ffffff;
    --night: #0b0f1c;
  }
  * { box-sizing: border-box; margin: 0; padding: 0; }
  html, body { width: 887px; height: 1200px; overflow: hidden; background: var(--white); }
  .flyer { position: relative; width: 887px; height: 1200px; overflow: hidden; font-family: "Lora", Georgia, serif; }

  .hero-photo {
    position: absolute; left: 0; top: 0; width: 887px; height: 680px;
    background: linear-gradient(100deg, #d9d2c8 0%, #f3efe9 25%, #fbfaf7 50%, #eef0ec 75%, #d7ddd3 100%);
  }
  .scene-photo {
    position: absolute; left: 0; top: 660px; width: 887px; height: 370px;
    background: linear-gradient(180deg, #c9ccd1 0%, #aab0b4 35%, #8f9a86 70%, #7f8d72 100%);
  }

  .tagline {
    position: absolute; left: 330px; top: 86px;
    font-family: "Great Vibes", cursive; font-weight: 400; font-size: 64px; line-height: 1;
    color: var(--brand-red);
    text-shadow: 1px 1px 0 var(--white), -1px -1px 0 var(--white), 1px -1px 0 var(--white), -1px 1px 0 var(--white), 0 3px 5px rgba(0,0,0,.3);
    white-space: nowrap;
  }
  .intro {
    position: absolute; left: 346px; top: 190px;
    font-style: italic; font-weight: 700; font-size: 20px; line-height: 29px; color: var(--ink);
    white-space: nowrap;
  }

  .swoosh { position: absolute; left: 0; top: 560px; width: 887px; height: 140px; }

  .photo-circle {
    position: absolute; border-radius: 50%; border: 9px solid var(--white);
    box-shadow: 0 4px 14px rgba(0,0,0,.3);
  }
  .photo-circle--left { left: 55px; top: 360px; width: 278px; height: 278px;
    background: linear-gradient(160deg, #6fb2e4 0%, #b9d5ea 45%, #8a6d5e 60%, #3d4f8c 100%); }
  .photo-circle--middle { left: 299px; top: 410px; width: 300px; height: 300px;
    background: linear-gradient(180deg, #3a8ad8 0%, #a9cff0 40%, #e9ecef 62%, #5b5f66 100%); }
  .photo-circle--right { left: 549px; top: 349px; width: 278px; height: 278px;
    background: linear-gradient(150deg, #f4f4f4 0%, #dcdcdc 45%, #3b3b3b 75%, #111 100%); }

  .panel { position: absolute; background: rgba(255,255,255,.55); }
  .panel__title { font-weight: 700; font-size: 18px; line-height: 24px; color: var(--ink); margin-bottom: 2px; }
  .dot-list { list-style: none; }
  .dot-list li { position: relative; font-weight: 700; color: var(--ink); white-space: nowrap; }
  .dot-list li::before {
    content: ""; position: absolute; border-radius: 50%; background: var(--brand-red);
  }

  .clients { left: 449px; top: 752px; width: 350px; height: 166px; padding: 12px 0 0 54px; }
  .clients .panel__title { margin-left: -49px; }
  .clients .dot-list li { font-size: 17.5px; line-height: 24.5px; }
  .clients .dot-list li::before { left: -41px; top: 6px; width: 13px; height: 13px; }

  .services { left: 36px; top: 728px; width: 390px; height: 160px; padding: 10px 0 0 16px; }
  .services .dot-list { column-count: 2; column-gap: 14px; padding-left: 20px; }
  .services .dot-list li { font-size: 15px; line-height: 25px; }
  .services .dot-list li::before { left: -18px; top: 8px; width: 10px; height: 10px; }

  .offer {
    position: absolute; left: 36px; top: 896px; width: 390px; height: 44px;
    background: var(--brand-red); color: var(--white);
    font-weight: 700; font-size: 16px; line-height: 44px; text-align: center;
    box-shadow: 0 3px 8px rgba(0,0,0,.25);
  }

  .brand {
    position: absolute; left: 40px; top: 956px; display: flex; align-items: center; gap: 12px;
  }
  .brand__dot { width: 50px; height: 50px; border-radius: 50%; background: var(--brand-blue); flex: none; }
  .brand__name { font-weight: 700; font-size: 22px; line-height: 26px; color: var(--white); text-shadow: 0 1px 3px rgba(0,0,0,.35); }

  .call-out {
    position: absolute; left: 501px; top: 966px;
    font-family: "Open Sans", Arial, sans-serif; font-size: 15.5px; line-height: 21px; color: var(--ink);
    white-space: nowrap;
  }

  .contact-band {
    position: absolute; left: 0; top: 1026px; width: 887px; height: 94px;
    background: linear-gradient(180deg, #2a7fd0 0%, var(--brand-blue) 45%, var(--brand-blue-dark) 100%);
  }
  .address {
    position: absolute; left: 74px; top: 24px; font-weight: 700; font-size: 16.5px; line-height: 24px; color: var(--white);
  }
  .phone-icon { position: absolute; left: 408px; top: -12px; width: 66px; height: 98px; }
  .phone-number {
    position: absolute; left: 487px; top: 12px;
    font-family: "Oswald", Impact, sans-serif; font-weight: 600; font-size: 52px; line-height: 1; color: var(--white);
    text-shadow: 0 3px 4px rgba(0,0,0,.45); letter-spacing: .5px;
  }

  .footer {
    position: absolute; left: 0; top: 1120px; width: 887px; height: 80px;
    background: linear-gradient(180deg, #1a1f2e 0%, var(--night) 100%);
  }
  .email {
    position: absolute; left: 72px; top: 22px; display: flex; align-items: center; gap: 16px;
    font-family: "Open Sans", Arial, sans-serif; font-size: 14.5px; color: var(--white);
  }
  .email svg { width: 20px; height: 14px; }
  .website { position: absolute; right: 66px; top: 20px; font-weight: 700; font-size: 18.5px; color: var(--white); }
</style>
</head>
<body>
<main class="flyer">
  <div class="hero-photo" role="img" aria-label="Photo of a bright room with large white-framed windows and a woman sipping a drink"></div>
  <div class="scene-photo" role="img" aria-label="Blurred photo of a modern building and lawn"></div>

  <h1 class="tagline">Experience Excellence</h1>
  <p class="intro">We are a commercial and<br>residential cleaning business,<br>supporting clients in the<br>greater Sydney area for<br>over 10 years.</p>

  <svg class="swoosh" viewBox="0 0 887 140" preserveAspectRatio="none" aria-hidden="true">
    <path d="M0 38 C260 20 600 10 887 14 L887 128 C600 100 300 110 0 120 Z" fill="var(--brand-red)"/>
    <path d="M0 120 C300 110 600 100 887 128 L887 136 C600 110 300 118 0 128 Z" fill="#8d97b3"/>
  </svg>

  <div class="photo-circle photo-circle--left" role="img" aria-label="Photo of a blue and brick apartment block"></div>
  <div class="photo-circle photo-circle--right" role="img" aria-label="Photo of a white modern lobby with floating staircase"></div>
  <div class="photo-circle photo-circle--middle" role="img" aria-label="Photo of a white apartment tower against a cloudy blue sky"></div>

  <section class="panel services">
    <h2 class="panel__title">Our services:</h2>
    <ul class="dot-list">
      <li>Building management</li>
      <li>Common area cleaning</li>
      <li>Window cleaning</li>
      <li>Lawn mowing</li>
      <li>Gardening</li>
      <li>Pressure cleaning</li>
      <li>Carpet cleaning</li>
      <li>Bin cleaning</li>
      <li>Handyman services</li>
    </ul>
  </section>

  <p class="offer">Keep this flyer: 15% off your first service!</p>

  <section class="panel clients">
    <h2 class="panel__title">Our clients include:</h2>
    <ul class="dot-list">
      <li>Strata Buildings</li>
      <li>Commercial Premises</li>
      <li>Construction Companies</li>
      <li>Restaurants and Clubs</li>
      <li>Doctor Surgeries</li>
    </ul>
  </section>

  <div class="brand">
    <span class="brand__dot"></span>
    <span class="brand__name">Silverleaf<br>upkeep services</span>
  </div>

  <p class="call-out">Call us now to see how we can help all your<br>cleaning and property maintenance needs.</p>

  <section class="contact-band">
    <p class="address">PO Box 417, Harbourview Heights,<br>NSW 2391, Australia</p>
    <svg class="phone-icon" viewBox="0 0 66 98" aria-hidden="true">
      <path d="M14 6 C4 10 2 20 4 34 C8 58 20 80 38 92 C46 97 54 95 60 88 L50 70 C47 66 43 66 40 69 L36 72 C28 64 22 50 20 38 L25 36 C29 34 30 30 29 26 L26 6 C24 2 18 3 14 6 Z" fill="var(--brand-red)" stroke="var(--white)" stroke-width="3"/>
    </svg>
    <p class="phone-number">0438 507 721</p>
  </section>

  <footer class="footer">
    <p class="email">
      <svg viewBox="0 0 20 14" aria-hidden="true">
        <rect x="1" y="1" width="18" height="12" fill="var(--white)"/>
        <path d="M1 1 L10 8 L19 1" fill="none" stroke="var(--night)" stroke-width="1.5"/>
      </svg>
      Info@silverleafupkeepservices.com.au
    </p>
    <p class="website">www.silverleafupkeepservices.com.au</p>
  </footer>
</main>
</body>
</html>
```